Civic Shieldpoint Company

We have design at www.vexaloft.com and want
New site design
Carallax
Images added
Were looking for your eyes. Just placement and look and feel. No hard coding. Design only.

Industry/Entity Type

It Company

```html
<!DOCTYPE html>
<html lang="en">
<head>
<meta charset="utf-8">
<title>Vexaloft — Identity Protection</title>
<link href="https://fonts.googleapis.com/css2?family=Arimo:wght@400;700&display=swap" rel="stylesheet">
<style>
:root{
  --red:#f0302c;
  --red-dark:#d92420;
  --ink:#1d1d1d;
  --charcoal:#3a3a3a;
  --dark-band:#404040;
  --gray-band:#e3e3e3;
  --gray-mid:#8a8a8a;
  --gray-row:#cfcfcf;
  --gray-light:#f1f1f1;
  --line:#d4d4d4;
  --white:#ffffff;
  --link:#2a7fc0;
}
*{box-sizing:border-box;margin:0;padding:0}
html,body{width:1200px;height:3550px;overflow:hidden}
body{position:relative;background:var(--white);font-family:"Arimo",Arial,sans-serif;color:var(--ink)}
.abs{position:absolute}

/* header */
.site-header{left:0;top:0;width:1200px;height:90px;background:var(--gray-light)}
.brand{left:94px;top:26px;font-size:40px;font-weight:700;color:var(--red);letter-spacing:-.5px}
.sign-in{right:48px;top:30px;width:106px;height:38px;background:var(--red);color:var(--white);font-size:19px;display:flex;align-items:center;justify-content:center}

/* hero */
.hero{left:0;top:90px;width:1200px;height:490px;background:linear-gradient(180deg,#7d7a72 0%,#a49d90 40%,#8d8a84 70%,#6f6d6a 100%)}
.hero-title,.hero-sub{background:rgba(0,0,0,.82);color:var(--white);padding:4px 10px}
.hero-title{left:86px;top:214px;font-size:40px}
.hero-sub{left:86px;top:268px;font-size:32px}
.hero-cta{left:88px;top:322px;background:var(--red);color:var(--white);font-size:22px;padding:8px 16px}
.crumb-bar{left:0;top:580px;width:1200px;height:44px;background:var(--red);color:var(--white);font-size:16px;text-align:right;padding:12px 28px 0 0}

/* features */
.feature{height:106px;display:flex;align-items:center}
.feature-red{left:236px;width:356px;background:var(--red);border-radius:53px 0 0 53px;color:var(--white);clip-path:polygon(0 0,100% 0,92% 100%,0 100%)}
.feature-dark{left:584px;width:376px;background:var(--charcoal);border-radius:0 53px 53px 0;color:var(--white);clip-path:polygon(7% 0,100% 0,100% 100%,0 100%,7% 50%)}
.feature-icon{width:86px;height:86px;border-radius:50%;background:var(--white);flex:none;display:flex;align-items:center;justify-content:center}
.feature-red .feature-icon{margin-left:10px}
.feature-dark .feature-icon{margin-right:10px}
.feature-text{font-size:13.5px;line-height:1.3;text-align:center;padding:0 14px}
.feature-red .feature-text{padding-right:30px}
.feature-dark .feature-text{padding-left:44px}
.feature-text h3{font-size:17px;font-weight:400;margin-bottom:4px}

.cta{background:var(--red);color:var(--white);font-size:50px;display:flex;align-items:center;justify-content:center;letter-spacing:.5px}

/* compare */
.compare-band{left:0;top:1290px;width:1200px;height:474px;background:var(--gray-band);border-top:2px solid #cbcbcb}
.compare-title{left:118px;top:1316px;font-size:45px;color:var(--charcoal);display:flex;align-items:center;gap:10px}
.compare-card{left:114px;top:1376px;width:972px;height:264px;background:var(--white);border:1px solid var(--line)}
.compare-table{left:122px;top:1386px;border-collapse:collapse;font-size:16px}
.compare-table td,.compare-table th{border:1px solid var(--line);text-align:center;font-weight:400;height:45px}
.compare-table th{height:46px}
.compare-table .row-label{text-align:left;padding-left:12px;width:160px}
.compare-table .corner{color:var(--red);text-align:center}
.compare-table .own{background:var(--red);color:var(--white);width:72px;border-color:var(--red);font-size:15px}
.compare-table .tall{height:62px;line-height:1.3}
.compare-table .rival{width:122px}
.own-pointer{left:282px;top:1620px}

.recovery{left:212px;top:1652px;width:866px;height:232px;background:#bcbcbc;border-radius:6px;overflow:hidden;font-size:15px;line-height:1.55}
.recovery h4{font-weight:400;font-size:18px;text-align:center;background:#c9c9c9;height:34px;line-height:34px;color:var(--charcoal)}
.recovery .assisted{background:#6b6b6b;color:var(--white);padding:4px 18px 10px}
.recovery .complete{background:#b5b5b5;color:var(--charcoal);padding:14px 18px}
.recovery em{font-style:normal;color:var(--red)}

/* command center */
.command-intro{left:212px;top:1928px;width:840px;font-size:19px;line-height:1.35;color:var(--ink)}
.command-list{left:206px;top:2002px;width:880px;list-style:none;font-size:15.5px;color:var(--link);line-height:1.3}
.command-list li{display:flex;gap:10px;margin-bottom:8px}
.command-list svg{flex:none;margin-top:1px}

/* dark section */
.dark-band{left:0;top:2200px;width:1200px;height:606px;background:var(--dark-band)}
.notch{left:560px;top:2198px}
.steps{background:var(--white);padding:10px 0}
.step{display:flex;align-items:center;gap:14px;padding:8px 16px;font-size:15px;line-height:1.2}
.step.gray{background:#c7c7c7;color:var(--ink)}
.step.light{background:var(--white);color:var(--red)}
.step.flip{flex-direction:row-reverse}
.num{width:58px;height:58px;border-radius:50%;background:var(--ink);color:var(--white);font-size:36px;display:flex;align-items:center;justify-content:center;flex:none}
.screen{background:linear-gradient(180deg,#fafafa,#e8ecef);border:8px solid #d8d8d8;box-shadow:0 2px 6px rgba(0,0,0,.4)}
.pin{width:32px;height:32px;border-radius:50%;background:var(--red);color:var(--white);font-size:17px;display:flex;align-items:center;justify-content:center}

.site-footer{left:0;top:3480px;width:1200px;height:70px;background:#2c2c2c;color:var(--white);font-size:16px;padding:26px 0 0 124px}
</style>
</head>
<body>

<header class="abs site-header"></header>
<div class="abs brand">Vexaloft</div>
<div class="abs sign-in">Sign In</div>

<section class="abs hero" role="img" aria-label="Busy city street crosswalk with pedestrians and yellow taxis"></section>
<h1 class="abs hero-title">Heading Title Goes here</h1>
<p class="abs hero-sub">Subheading sentence goes here</p>
<a class="abs hero-cta">LEARN MORE</a>
<nav class="abs crumb-bar">Home / User Agreement / Privacy Policy</nav>

<!-- features -->
<div class="abs feature feature-red" style="top:702px">
  <span class="feature-icon"><svg width="52" height="52" viewBox="0 0 52 52"><circle cx="20" cy="20" r="13" fill="none" stroke="#f0302c" stroke-width="6"/><line x1="30" y1="30" x2="46" y2="46" stroke="#f0302c" stroke-width="8" stroke-linecap="round"/></svg></span>
  <div class="feature-text"><h3>ID Monitoring &amp; Surveillance</h3>Scanning engines, human intelligence gathering and mathematical algorithms find<br>[learn more]</div>
</div>
<div class="abs feature feature-dark" style="top:702px">
  <div class="feature-text"><h3>Identity Recovery Theft</h3>If your identity is stolen, we recover your ID for you or assist you in your recovery -<br>[learn more]</div>
  <span class="feature-icon"><svg width="50" height="50" viewBox="0 0 50 50"><circle cx="25" cy="15" r="10" fill="#3a3a3a"/><path d="M6 48 Q8 28 25 28 Q42 28 44 48Z" fill="#3a3a3a"/></svg></span>
</div>

<div class="abs feature feature-red" style="top:838px">
  <span class="feature-icon"><svg width="50" height="50" viewBox="0 0 50 50"><text x="25" y="40" text-anchor="middle" font-family="Arimo, Arial, sans-serif" font-size="44" fill="#f0302c">$</text></svg></span>
  <div class="feature-text"><h3>$25,000 Loss Insurance</h3>Identity Fraud Loss and Expense Reimbursement Master Policy from Norvane Insur-<br>[learn more]</div>
</div>
<div class="abs feature feature-dark" style="top:838px">
  <div class="feature-text"><h3>ID vs Credit Monitoring</h3>If your identity is stolen, we recover your ID for you or assist you in your recovery -<br>[learn more]</div>
  <span class="feature-icon"><svg width="56" height="40" viewBox="0 0 56 40"><path d="M2 20 Q28 -8 54 20 Q28 48 2 20Z" fill="#3a3a3a"/><circle cx="28" cy="20" r="9" fill="#fff"/><circle cx="28" cy="20" r="5" fill="#3a3a3a"/></svg></span>
</div>

<div class="abs feature feature-red" style="top:974px">
  <span class="feature-icon"><svg width="52" height="52" viewBox="0 0 52 52"><circle cx="20" cy="20" r="13" fill="none" stroke="#f0302c" stroke-width="6"/><line x1="30" y1="30" x2="46" y2="46" stroke="#f0302c" stroke-width="8" stroke-linecap="round"/></svg></span>
  <div class="feature-text"><h3>ID Monitoring &amp; Surveillance</h3>Scanning engines, human intelligence gathering and mathematical algorithms find<br>[learn more]</div>
</div>
<div class="abs feature feature-dark" style="top:974px">
  <div class="feature-text"><h3>Faces of ID Theft</h3>Criminals use sophisticated methods to obtain and misuse our personal<br>[learn more]</div>
  <span class="feature-icon"><svg width="50" height="50" viewBox="0 0 50 50"><path d="M10 18 L40 18 L36 6 L14 6Z" fill="#3a3a3a"/><rect x="4" y="17" width="42" height="4" fill="#3a3a3a"/><circle cx="25" cy="28" r="7" fill="#3a3a3a"/><path d="M8 48 Q10 34 25 34 Q40 34 42 48Z" fill="#3a3a3a"/></svg></span>
</div>

<a class="abs cta" style="left:426px;top:1124px;width:391px;height:106px">GET STARTED</a>

<!-- compare -->
<section class="abs compare-band"></section>
<h2 class="abs compare-title">Compare Protection
  <svg width="26" height="32" viewBox="0 0 26 32"><path d="M6 14 V9 A7 7 0 0 1 20 9 V14" fill="none" stroke="#b5b5b5" stroke-width="4"/><rect x="2" y="14" width="22" height="17" rx="2" fill="#b5b5b5"/></svg>
</h2>
<div class="abs compare-card"></div>
<table class="abs compare-table">
  <tr><th class="row-label corner">Comparison Table</th><th class="own">Vexaloft</th><th class="rival">Lockwell</th><th class="rival">Identity Ward</th><th class="rival">ID Bastion</th><th class="rival">TrueMark ID</th><th class="rival">ID Sentry</th><th class="rival">Creditline</th></tr>
  <tr><td class="row-label">Subscription Cost</td><td class="own">$4.15/mo</td><td>$34.50/mo</td><td>$35.98/mo</td><td>$36.95/mo</td><td>$16.99/mo</td><td>$39.90/mo</td><td>$29.90/mo</td></tr>
  <tr><td class="row-label">Adults Covered</td><td class="own">All</td><td>2</td><td>2</td><td>2</td><td>2</td><td>2</td><td>2</td></tr>
  <tr><td class="row-label">Children Covered</td><td class="own">All</td><td>2</td><td>0</td><td>4</td><td>4</td><td>0</td><td>0</td></tr>
  <tr><td class="row-label tall">Level of Assistance</td><td class="own tall">Complete Restoration</td><td class="tall">Assisted</td><td class="tall">Assisted</td><td class="tall">Complete Restoration</td><td class="tall">Assisted</td><td class="tall">Complete Restoration</td><td class="tall">Assisted</td></tr>
</table>
<svg class="abs own-pointer" width="74" height="64" viewBox="0 0 74 64"><path d="M0 0 H74 V40 L37 64 L0 40Z" fill="#f0302c"/></svg>

<div class="abs recovery">
  <h4>Types of Recovery</h4>
  <p class="assisted"><em>Assisted Recovery</em> - This means the organization will assist you in recovering your ID. This is accomplished through coaching, providing details of the agencies you need to contact, forms, etc. You are the person applying the effort to restore your identity. This will require countless hours of your time. Better than nothing.</p>
  <p class="complete"><em>Complete Restoration</em> - This means the organization will act on your behalf to restore your identity for you. This is accomplished by signing paperwork giving the recovery specialist the ability to act on your behalf and work for you to recover your identity to pre-theft status. This requires minimal effort as they do the work for you. The Best Choice!</p>
</div>

<!-- command center -->
<p class="abs command-intro">The ID Command Center provides a real-time view of your automated identity monitoring and alerts, access to your lost wallet protection, your policy coverage and more.</p>
<ul class="abs command-list">
  <li><svg width="18" height="18" viewBox="0 0 18 18"><rect x="1" y="1" width="16" height="16" fill="none" stroke="#f0302c" stroke-width="2"/><path d="M4 9 L8 13 L15 3" fill="none" stroke="#f0302c" stroke-width="2.5"/></svg>View your ID Monitoring and Surveillance status with alerts, and respond to any suspicious information with a click.</li>
  <li><svg width="18" height="18" viewBox="0 0 18 18"><rect x="1" y="1" width="16" height="16" fill="none" stroke="#f0302c" stroke-width="2"/><path d="M4 9 L8 13 L15 3" fill="none" stroke="#f0302c" stroke-width="2.5"/></svg>Create and update your Lost Wallet Protection service to be ready when you need it.</li>
  <li><svg width="18" height="18" viewBox="0 0 18 18"><rect x="1" y="1" width="16" height="16" fill="none" stroke="#f0302c" stroke-width="2"/><path d="M4 9 L8 13 L15 3" fill="none" stroke="#f0302c" stroke-width="2.5"/></svg>Access to your family Norvane Personal Loss Policy Coverage including protection description.</li>
  <li><svg width="18" height="18" viewBox="0 0 18 18"><rect x="1" y="1" width="16" height="16" fill="none" stroke="#f0302c" stroke-width="2"/><path d="M4 9 L8 13 L15 3" fill="none" stroke="#f0302c" stroke-width="2.5"/></svg>Contact Fully Managed Restoration in the event of suspicious information or ID theft.</li>
  <li><svg width="18" height="18" viewBox="0 0 18 18"><rect x="1" y="1" width="16" height="16" fill="none" stroke="#f0302c" stroke-width="2"/><path d="M4 9 L8 13 L15 3" fill="none" stroke="#f0302c" stroke-width="2.5"/></svg>Initiate analysis and as needed, Fully Managed Recovery for you or a family member of any suspicious inquiries or possible identity theft incidents.</li>
</ul>

<!-- dark section -->
<section class="abs dark-band"></section>
<svg class="abs notch" width="80" height="34" viewBox="0 0 80 34"><path d="M0 0 H80 L40 34Z" fill="#ffffff"/></svg>

<div class="abs steps" style="left:47px;top:2276px;width:522px;height:400px">
  <div class="step gray"><span class="num">1</span><span>Account Status information identifies the type of account, your account ID number and your protection status. In addition, quick view your identity monitoring status results. Green means no new alerts. Red means new alerts found.</span></div>
  <div class="step light flip"><span class="num">2</span><span>Message and task center provides you with notice there are messages to review or tasks that warrant your attention or action. Messages or tasks display here when issued. Subscribers are also emailed new alert notices.</span></div>
  <div class="step gray"><span class="num">3</span><span>3. Identity monitoring controls provides subscribers with choices on how to monitor their ID. In addition, more detailed explanation of monitoring, your information being monitored and monitoring history.</span></div>
  <div class="step light flip"><span class="num">4</span><span>4. Identity theft report submission allows subscribers to file a report if they suspect any activity within their identity that they do not recognize. Reports are reviewed by a specialist. If a true event, a recovery specialist will be assigned to your case. If you suspect you are a victim of identity theft, call the toll-free number immediately.</span></div>
</div>

<div class="abs screen" role="img" aria-label="Privacy Command Center dashboard screen with numbered callouts" style="left:611px;top:2284px;width:544px;height:380px"></div>
<span class="abs pin" style="left:842px;top:2364px">1</span>
<span class="abs pin" style="left:1024px;top:2376px">2</span>
<span class="abs pin" style="left:858px;top:2452px">3</span>
<span class="abs pin" style="left:940px;top:2452px">4</span>

<!-- lower section -->
<div class="abs screen" role="img" aria-label="Privacy Command Center dashboard screen with numbered callouts" style="left:123px;top:2864px;width:438px;height:366px"></div>
<span class="abs pin" style="left:348px;top:2984px">7</span>
<span class="abs pin" style="left:466px;top:2972px">8</span>
<span class="abs pin" style="left:278px;top:3086px">5</span>
<span class="abs pin" style="left:390px;top:3088px">6</span>

<div class="abs steps" style="left:608px;top:2840px;width:524px;height:408px;border:1px solid var(--line)">
  <div class="step gray"><span class="num">5</span><span>Lost wallet service setup and update process is there when you need it. If you lose your wallet or purse, call the toll-free number and have a recovery specialist working on your behalf. In addition, set up credit fraud alerts or freeze your credit to eliminate any misuse.</span></div>
  <div class="step light flip"><span class="num">6</span><span>Personal loss insurance coverage details and explanation, subscriber policy number and information, insurance company toll-free number to submit claims and process to monitor claim status.</span></div>
  <div class="step gray"><span class="num">7</span><span>Red alert notice recognizes there is a new source of information found during the identity monitoring and surveillance. Simply click to view the alert and to provide response.</span></div>
  <div class="step light flip"><span class="num">8</span><span>Red messages or tasks brought to the subscribers attention. Click to review and determine if known information or not. If not, a single click will start the ball rolling to investigate this information further by a recovery specialist.</span></div>
</div>

<a class="abs cta" style="left:426px;top:3280px;width:391px;height:108px">GET STARTED</a>

<footer class="abs site-footer">Home / User Agreement / Privacy Policy</footer>

</body>
</html>
```